Business Card Design for a Lending Business (Hard Money loans)

We need a business card for our Real Estate Lending business. We do hard Money loans for real estate investors. We have an existing logo we like, see attached. I'd like the business card to mostly include the logo colors, but a bright color pop of some sort would be nice to see also. Card should include Logo, Company Name, Company Address, Employee Name, Cell Phone, Main Phone, Email, Website

Industry/Entity Type

Finance / Lending

Contact Information for Business Card

Logo, Company Name, Company Address, Employee Name, Cell Phone, Main Phone, Email, Website

Requirements
Nice to have
• I'd like the business card to mostly include the logo colors, but a bright color pop of some sort would be nice to see also.

```html
<!DOCTYPE html>
<html lang="en">
<head>
<meta charset="utf-8">
<title>Harbor Crest Lending – Business Card</title>
<link href="https://fonts.googleapis.com/css2?family=Lato:wght@400;700&family=Montserrat:wght@700;800&display=swap" rel="stylesheet">
<style>
  :root {
    --navy: #062a8c;
    --sky: #1fa6e0;
    --paper: #f3f3f3;
    --ink: #111111;
    --stage: #2b2b2b;
  }
  * { box-sizing: border-box; margin: 0; padding: 0; }
  html, body {
    width: 1200px; height: 1200px; overflow: hidden;
    background: var(--stage);
  }
  .sheet {
    width: 1200px; height: 1200px;
    display: flex; align-items: center; justify-content: center; gap: 60px;
  }
  .card {
    width: 420px; height: 735px;
    position: relative;
    display: flex; flex-direction: column; align-items: center;
  }
  .card--front { background: var(--navy); justify-content: center; }
  .card--back { background: var(--paper); padding: 70px 52px 0; align-items: flex-start; }

  .brand {
    display: flex; flex-direction: column; align-items: center; gap: 22px;
    font-family: "Montserrat", sans-serif; font-weight: 800;
    text-align: center; line-height: 1.1; letter-spacing: 0.12em;
  }
  .brand__dot { width: 96px; height: 96px; border-radius: 50%; }
  .brand__name { font-size: 34px; }
  .brand__name small { display: block; font-size: 34px; }
  .card--front .brand { color: #ffffff; margin-top: -60px; }
  .card--front .brand__dot { background: var(--sky); }
  .card--back .brand { color: var(--navy); align-self: center; }
  .card--back .brand__dot { background: var(--navy); }

  .person { margin-top: 58px; }
  .person__name {
    font-family: "Montserrat", sans-serif; font-weight: 800;
    color: var(--navy); font-size: 36px; letter-spacing: 0.02em; line-height: 1;
  }
  .person__role {
    font-family: "Lato", sans-serif; font-size: 15px; color: var(--ink);
    letter-spacing: 0.04em; margin-top: 6px;
  }
  .address {
    font-family: "Lato", sans-serif; font-size: 21px; color: var(--ink);
    font-style: normal; line-height: 1.3; margin-top: 24px;
  }
  .contacts { list-style: none; margin-top: 18px; font-family: "Lato", sans-serif; font-size: 21px; color: var(--ink); }
  .contacts li { display: flex; align-items: center; gap: 12px; line-height: 1.55; }
  .contacts svg { width: 18px; height: 18px; flex: none; fill: var(--sky); }
  .accent { color: var(--sky); }
</style>
</head>
<body>
<main class="sheet">
  <section class="card card--front" aria-label="Card front">
    <div class="brand">
      <span class="brand__dot"></span>
      <div class="brand__name">HARBOR CREST<small>LENDING</small></div>
    </div>
  </section>

  <section class="card card--back" aria-label="Card back">
    <div class="brand">
      <span class="brand__dot"></span>
      <div class="brand__name">HARBOR CREST<small>LENDING</small></div>
    </div>

    <div class="person">
      <h1 class="person__name">DANA ORTIZ</h1>
      <p class="person__role">MANAGER</p>
    </div>

    <address class="address">1820 Millbrook Lane<br>Riverton, MD 21400</address>

    <ul class="contacts">
      <li>
        <svg viewBox="0 0 24 24" aria-hidden="true"><path d="M7 1h10a2 2 0 0 1 2 2v18a2 2 0 0 1-2 2H7a2 2 0 0 1-2-2V3a2 2 0 0 1 2-2zm0 3v14h10V4H7zm5 15.5a1.2 1.2 0 1 0 0 2.4 1.2 1.2 0 0 0 0-2.4z"/></svg>
        410-555-0142
      </li>
      <li>
        <svg viewBox="0 0 24 24" aria-hidden="true"><path d="M6.6 10.8a15.2 15.2 0 0 0 6.6 6.6l2.2-2.2a1 1 0 0 1 1-.25 11.4 11.4 0 0 0 3.6.57 1 1 0 0 1 1 1V20a1 1 0 0 1-1 1A17 17 0 0 1 3 4a1 1 0 0 1 1-1h3.5a1 1 0 0 1 1 1c0 1.25.2 2.45.57 3.6a1 1 0 0 1-.25 1z"/></svg>
        410-555-0187
      </li>
      <li>
        <svg viewBox="0 0 24 24" aria-hidden="true"><path d="M2 5h20v14H2V5zm2 2v.5l8 5 8-5V7l-8 5-8-5z"/></svg>
        info@harborcrestlending.com
      </li>
      <li>
        <svg viewBox="0 0 24 24" aria-hidden="true"><circle cx="12" cy="12" r="10"/></svg>
        <span>www.<span class="accent">harborcrestlending</span>.com</span>
      </li>
    </ul>
  </section>
</main>
</body>
</html>
```